Packaging design for high end, natural skin care line needed

Marisol Thackery Beauty needs a label design. It is a new skin care line I am launching.
For years my line Velvet Orchard Beauty was quite popular and featured in several magazines, but for personal reasons had to be shut down. Now I am launching a new line featuring VOB's top selling products, but focused solely on skin care more so than cosmetics. All products will still be handmade, but the line should still look professional-something worthy of a Brindle Market shelf!
I am branding it with my name, as I am often quoted in articles related to gluten in beauty products, so Marisol Thackery and beauty are key words.
The key products will be facial and body serums which are packaged in .5oz., 1oz. and larger amber glass bottles with black dropper tops, I will include pictures below. For dimensions, the labels can be any size that you think will work best, but need to at the least fit the 1oz. bottle, dimensions shown here http://www.corvelflask.example/amber-glass-tall-round-flask/p/QZ7K-93/
I loved the former VOB logo, but for Marisol Thackery Beauty I am looking for something more personal, more apothecary-like, and probably less colorful.
The line will be small, just a handful of products, but luxe, rich.
I am attaching photos of Velvet Orchard Beauty's packaging for your reference.
Thanks much!!

Hi Everyone! Thank you for your submissions! Please see the links I provided in the brief, I really am looking for something more technical looking, like an apothecary. And want black text on a white background, not a black background, and nothing flowery.
Thank you all!!
Marisol

Target Market(s)

My clients are primarily women of all ages, but with more of a skin care focus, and no longer a cosmetic one, I would also like to appeal to a male audience. My clients are health conscious, gluten-free, natural, paleo, or vegan, etc. Target age is probably 25-55. Products are a bit high end, priced $45-65.

Industry/Entity Type

Cosmetics

Requirements
Must have
• It must at least say Marisol Thackery, or can say Marisol Thackery Beauty, but "Beauty" is not necessary. And capitalization is open, try whatever you think serves the brand. Likely slogans or taglines that can be included but are not essential: Care for your skin. Love and care for your skin. Handmade with love in the USA. Handmade in the USA. Think modern day apothecary. Small batch scotch. Something fine, but custom, handmade.
Nice to have
• I like the aesthetic of Oribel Skin Care a bit http://www.oribelhollis.example.au/
And of Dorian Valtz as shown here http://www.pinboardia.example/pin/847302915563017442/
Also of something like this that is even customizable http://www.pinboardia.example/pin/58274106392285514/
Every product is handmade in small batches, with fine ingredients, a moderate price point of around $45-$65. And I will likely begin making custom orders. So there could be a space to say when it was made, or for whom. I would like to keep the colors classic though, I probably want to stay away from the bright pink on this one.
Should not have
• As I mentioned, probably want to stay away from a lot of color. I like black vs. gray for the text, as it will show up better in editorials. I must look good, but also photograph well. Thanks!

```html
<!DOCTYPE html>
<html lang="en">
<head>
<meta charset="utf-8">
<title>Marisol Thackery – Facial &amp; Body Serums Label</title>
<link href="https://fonts.googleapis.com/css2?family=Montserrat:wght@400;600;700&display=swap" rel="stylesheet">
<style>
  :root {
    --ink: #1a1a1a;
    --paper: #ffffff;
    --muted: #9a9a9a;
    --edge: #cfcfcf;
    --bg-center: #ffffff;
    --bg-outer: #dcdcdc;
  }
  html, body {
    margin: 0;
    padding: 0;
    overflow: hidden;
  }
  h1, h2, h3, p { margin: 0; }
  .canvas {
    position: relative;
    width: 1200px;
    height: 1000px;
    overflow: hidden;
    background: radial-gradient(ellipse at 55% 40%, var(--bg-center) 0%, #f3f3f3 45%, var(--bg-outer) 100%);
    font-family: "Montserrat", sans-serif;
    color: var(--ink);
  }

  /* Brand marks */
  .brand-mark {
    position: absolute;
    display: flex;
    align-items: center;
    justify-content: center;
    border-radius: 50%;
    text-align: center;
    box-sizing: border-box;
  }
  .brand-mark--primary {
    left: 639px; top: 109px;
    width: 162px; height: 162px;
    background: var(--ink);
  }
  .brand-mark--primary .brand-mark__name {
    color: var(--paper);
    font-weight: 700;
    font-size: 18px;
    letter-spacing: 1px;
    line-height: 1.25;
    text-transform: uppercase;
  }
  .brand-mark--partner {
    left: 930px; top: 144px;
    width: 146px; height: 146px;
    border: 3px solid var(--ink);
  }
  .brand-mark--partner .brand-mark__name {
    color: var(--ink);
    font-weight: 700;
    font-size: 14px;
    letter-spacing: 1px;
    line-height: 1.3;
    text-transform: uppercase;
  }

  /* Label artwork */
  .label {
    position: absolute;
    left: 550px; top: 315px;
    width: 600px; height: 300px;
    background: var(--paper);
    border: 1px solid var(--edge);
    box-sizing: border-box;
  }
  .label__badge {
    position: absolute;
    left: 33px;
    width: 74px; height: 74px;
    border-radius: 50%;
    display: flex;
    align-items: center;
    justify-content: center;
    box-sizing: border-box;
    text-align: center;
    border: 2px solid var(--ink);
  }
  .label__badge--partner { top: 28px; }
  .label__badge--partner span {
    font-size: 7.5px;
    font-weight: 700;
    line-height: 1.3;
    text-transform: uppercase;
    color: var(--ink);
  }
  .label__badge--handmade { top: 156px; }
  .label__size {
    position: absolute;
    left: 55px; top: 260px;
    font-size: 16px;
    line-height: 1;
  }
  .label__logo {
    position: absolute;
    left: 274px; top: 29px;
    width: 98px; height: 98px;
    border-radius: 50%;
    background: var(--ink);
    color: var(--paper);
    display: flex;
    align-items: center;
    justify-content: center;
    text-align: center;
    font-size: 11px;
    font-weight: 700;
    line-height: 1.25;
    text-transform: uppercase;
  }
  .label__name {
    position: absolute;
    left: 155px; top: 130px;
    width: 330px;
    text-align: center;
    font-size: 22px;
    font-weight: 700;
    letter-spacing: 2px;
    line-height: 1.15;
    text-transform: uppercase;
  }
  .label__product {
    position: absolute;
    left: 155px; top: 192px;
    width: 328px;
    border-top: 1.5px solid var(--ink);
    border-bottom: 1.5px solid var(--ink);
    text-align: center;
    font-size: 20px;
    font-weight: 700;
    letter-spacing: 0.5px;
    line-height: 1.2;
    padding: 3px 0 3px;
    text-transform: uppercase;
  }
  .label__description {
    position: absolute;
    left: 155px; top: 236px;
    width: 328px;
    font-size: 8.6px;
    line-height: 14px;
    text-align: justify;
  }
  .label__info {
    position: absolute;
    left: 505px; top: 36px;
    width: 80px;
    font-size: 8.6px;
    line-height: 1.4;
  }
  .label__info h3 {
    font-size: 8.6px;
    font-weight: 600;
    color: var(--ink);
  }
  .label__info p {
    margin-bottom: 10px;
    color: var(--muted);
  }
</style>
</head>
<body>
<main class="canvas">

  <div class="brand-mark brand-mark--primary">
    <span class="brand-mark__name">Marisol<br>Thackery</span>
  </div>

  <div class="brand-mark brand-mark--partner">
    <span class="brand-mark__name">Velvet<br>Orchard<br>Beauty</span>
  </div>

  <section class="label">
    <div class="label__badge label__badge--partner">
      <span>Velvet<br>Orchard<br>Beauty</span>
    </div>
    <div class="label__badge label__badge--handmade" role="img" aria-label="Handmade certification seal"></div>
    <div class="label__size">5oz</div>

    <div class="label__logo">Marisol<br>Thackery</div>
    <h1 class="label__name">Marisol<br>Thackery</h1>
    <h2 class="label__product">Facial &amp; Body Serums</h2>
    <p class="label__description">Marisol Thackery serum is rich in antioxidants, omega 6 fatty acids and vitamin E. It also contains saponins, which minimize wrinkles and helps to calm inflammation caused by acne and exzema. Regular use helps skin maintain a youthful glow. For all skin types.</p>

    <div class="label__info">
      <h3>Directions:</h3>
      <p>After cleansing, Apply 3-6 drops to clean finger tips/palms and gently pat onto face and neck in upward circular motions. Finish with appropriate moisturizer.</p>
      <h3>Ingredients:</h3>
      <p>Certified organic argan oil.</p>
      <p>Made in USA.</p>
    </div>
  </section>

</main>
</body>
</html>
```